Logo & Visitenkarte für KochWinkelhof
Zielgruppe
Die Jausenstation mit Hausmannskost
Aufgabenstellung
Telefonnummer 0517 649013
E-Mail kochwinkelhof@postfach-beispiel.at
Und den Firmennamen

```html
<!DOCTYPE html>
<html lang="de">
<head>
<meta charset="utf-8">
<title>KochWinkelhof – Visitenkarte</title>
<link rel="stylesheet" href="https://fonts.googleapis.com/css2?family=Oswald:wght@300;400&display=swap">
<style>
  :root {
    --backdrop: #cdd1d4;
    --card: #000000;
    --accent: #a4b82a;
    --ink: #ffffff;
    --rule: #6b6b6b;
    --ring: #8a8a8a;
  }
  html, body {
    margin: 0;
    padding: 0;
    width: 1200px;
    height: 1194px;
    overflow: hidden;
    background: var(--backdrop);
  }
  .canvas {
    position: relative;
    width: 1200px;
    height: 1194px;
    font-family: "Oswald", "Arial Narrow", sans-serif;
    font-weight: 300;
  }
  .card {
    position: absolute;
    left: 254px;
    width: 696px;
    height: 396px;
    background: var(--card);
    color: var(--ink);
  }
  .card--front { top: 146px; }
  .card--back  { top: 648px; }

  .front-brand {
    position: absolute;
    left: 0;
    right: 0;
    top: 160px;
    display: flex;
    align-items: center;
    justify-content: center;
    gap: 18px;
  }
  .front-brand__dot {
    width: 56px;
    height: 56px;
    border: 3px solid var(--ring);
    border-radius: 50%;
    box-sizing: border-box;
  }
  .front-brand__name {
    font-size: 58px;
    font-weight: 400;
    color: var(--accent);
    line-height: 1;
  }

  .back-name {
    position: absolute;
    left: 76px;
    top: 96px;
    margin: 0;
    font-size: 34px;
    font-weight: 400;
    color: var(--accent);
    line-height: 1;
  }
  .back-tagline {
    position: absolute;
    left: 76px;
    top: 156px;
    margin: 0;
    font-size: 18px;
    letter-spacing: 0.3px;
    text-transform: uppercase;
  }
  .back-rule {
    position: absolute;
    left: 76px;
    top: 210px;
    width: 500px;
    height: 1px;
    background: var(--rule);
  }
  .contact {
    position: absolute;
    left: 76px;
    display: flex;
    gap: 16px;
    font-size: 16px;
    line-height: 28px;
    text-transform: uppercase;
    letter-spacing: 0.3px;
  }
  .contact--phone { top: 238px; }
  .contact--address { top: 278px; }
  .contact__icon {
    width: 20px;
    height: 28px;
    flex: none;
  }
  .contact__text { margin: 0; }
</style>
</head>
<body>
<div class="canvas">
  <section class="card card--front">
    <div class="front-brand">
      <span class="front-brand__dot"></span>
      <span class="front-brand__name">KochWinkelhof</span>
    </div>
  </section>

  <section class="card card--back">
    <h1 class="back-name">KochWinkelhof</h1>
    <p class="back-tagline">Die Jausenstation mit Hausmannskost</p>
    <div class="back-rule"></div>

    <div class="contact contact--phone">
      <svg class="contact__icon" viewBox="0 0 20 28" aria-hidden="true">
        <path fill="#ffffff" d="M5 6c1-1 2-1 3 0l2 3c.6 1 .4 2-.4 2.6l-1.2.9c.8 2.4 2.2 4.2 4.2 5.6l1-1.1c.7-.8 1.8-.9 2.6-.2l2.4 2.1c.9.8.9 2 0 2.8l-1.2 1.2C15 25 6 19 3.6 10.5 3.2 8.9 3.8 7.2 5 6z"/>
      </svg>
      <p class="contact__text">0517 649013</p>
    </div>

    <div class="contact contact--address">
      <svg class="contact__icon" viewBox="0 0 20 28" aria-hidden="true">
        <path fill="#ffffff" d="M10 3a7 7 0 0 0-7 7c0 5 7 13 7 13s7-8 7-13a7 7 0 0 0-7-7zm0 10a3 3 0 1 1 0-6 3 3 0 0 1 0 6z"/>
      </svg>
      <p class="contact__text">Birkenauer Str. 112<br>9400 Murnfeld am See<br>Österreich</p>
    </div>
  </section>
</div>
</body>
</html>
```